4nowvanta business card
4nowvanta busines card
Professional
Lucinda Harwell Brophy
Principal Partner
42 Juniper Street
Arlington, MA 02319
lucinda@4nowvanta.com
www.4nowvanta.com
I uploaded the full folder, because I was having a little trouble saving the .ai and .eps files

```html
<!DOCTYPE html>
<html lang="en">
<head>
<meta charset="utf-8">
<title>4nowvanta stationery set</title>
<link rel="stylesheet" href="https://fonts.googleapis.com/css2?family=Open+Sans:wght@400;600;700&display=swap">
<style>
  :root {
    --board: #3d3e40;
    --navy: #14237a;
    --navy-deep: #0b1552;
    --green: #1f9a3a;
    --paper: #ffffff;
    --ink: #4a4a4a;
    --label: #8a8b8d;
  }
  html, body { margin: 0; padding: 0; overflow: hidden; }
  body {
    width: 1200px; height: 312px;
    background: var(--board);
    font-family: "Open Sans", Arial, sans-serif;
    position: relative;
  }
  .piece {
    position: absolute;
    background: var(--paper);
    box-shadow: 0 1px 3px rgba(0,0,0,.45);
    overflow: hidden;
  }
  .piece svg { position: absolute; left: 0; top: 0; width: 100%; height: 100%; }
  .brand { position: absolute; font-weight: 700; color: var(--navy); line-height: 1; white-space: nowrap; }
  .brand.on-dark { color: var(--paper); }
  .label {
    position: absolute; font-size: 5px; color: var(--label);
    letter-spacing: .3px; text-transform: uppercase; white-space: nowrap;
  }
  .contact { position: absolute; color: var(--ink); line-height: 1.35; white-space: nowrap; }

  /* business cards */
  .card { width: 86px; height: 41px; }
  .card .brand { left: 6px; top: 6px; font-size: 5px; }
  .card .contact { font-size: 3px; }

  /* letterheads */
  .letterhead { width: 197px; height: 249px; top: 34px; }
  .letterhead .brand { left: 13px; top: 32px; font-size: 6px; }
  .letterhead .contact { font-size: 3.2px; left: 0; right: 0; bottom: 12px; text-align: center; }

  /* envelopes */
  .envelope { width: 207px; height: 105px; }
  .envelope .brand { left: 9px; top: 17px; font-size: 5px; }
  .envelope .contact { font-size: 3px; left: 9px; top: 27px; }

  .envelope-back { width: 219px; height: 86px; left: 914px; }
  .envelope-back .brand { left: 50%; transform: translateX(-50%); top: 14px; font-size: 5px; }
</style>
</head>
<body>
<svg width="0" height="0" style="position:absolute">
  <defs>
    <linearGradient id="navyFade" x1="0" y1="0" x2="1" y2="0">
      <stop offset="0" stop-color="#0b1552"/>
      <stop offset="1" stop-color="#1c2f95"/>
    </linearGradient>
  </defs>
</svg>

<!-- Business cards -->
<div class="piece card" style="left:19px;top:108px">
  <svg viewBox="0 0 86 41" preserveAspectRatio="none">
    <path d="M0 0H86V24C60 20 30 30 0 22Z" fill="url(#navyFade)"/>
    <path d="M0 22C30 30 60 20 86 24V25.5C60 22 30 32 0 23.5Z" fill="var(--green)"/>
  </svg>
  <div class="brand on-dark">4nowvanta</div>
</div>
<div class="piece card" style="left:115px;top:108px">
  <svg viewBox="0 0 86 41" preserveAspectRatio="none">
    <path d="M0 0H86V10C60 7 30 14 0 9Z" fill="url(#navyFade)"/>
    <path d="M0 9C30 14 60 7 86 10V11.3C60 8.5 30 15.5 0 10.3Z" fill="var(--green)"/>
  </svg>
  <div class="brand" style="top:15px">4nowvanta</div>
  <div class="contact" style="left:40px;top:24px">Lucinda Harwell Brophy<br>Principal Partner</div>
</div>
<div class="piece card" style="left:19px;top:158px">
  <svg viewBox="0 0 86 41" preserveAspectRatio="none">
    <path d="M0 35C30 39 60 31 86 34V41H0Z" fill="url(#navyFade)"/>
  </svg>
  <div class="brand">4nowvanta</div>
  <div class="contact" style="left:6px;top:16px">42 Juniper Street<br>Arlington, MA 02319</div>
</div>
<div class="piece card" style="left:115px;top:158px">
  <svg viewBox="0 0 86 41" preserveAspectRatio="none">
    <path d="M0 35C30 39 60 31 86 34V41H0Z" fill="url(#navyFade)"/>
  </svg>
  <div class="contact" style="left:6px;top:10px">lucinda@4nowvanta.com<br>www.4nowvanta.com</div>
</div>

<!-- Letterheads -->
<div class="piece letterhead" style="left:216px">
  <svg viewBox="0 0 197 249" preserveAspectRatio="none">
    <path d="M0 0H197V28C150 20 80 8 0 22Z" fill="url(#navyFade)"/>
    <path d="M0 22C80 8 150 20 197 28V30C150 22 80 11 0 24Z" fill="var(--green)"/>
  </svg>
  <div class="brand">4nowvanta</div>
  <div class="contact">42 Juniper Street, Arlington, MA 02319<br>lucinda@4nowvanta.com · www.4nowvanta.com</div>
</div>
<div class="label" style="left:282px;top:288px">Letterhead One</div>

<div class="piece letterhead" style="left:439px">
  <svg viewBox="0 0 197 249" preserveAspectRatio="none">
    <path d="M0 0H197V28C150 20 80 8 0 22Z" fill="url(#navyFade)"/>
    <path d="M0 22C80 8 150 20 197 28V30C150 22 80 11 0 24Z" fill="var(--green)"/>
  </svg>
  <div class="brand">4nowvanta</div>
  <div class="contact">42 Juniper Street, Arlington, MA 02319<br>lucinda@4nowvanta.com · www.4nowvanta.com</div>
</div>
<div class="label" style="left:506px;top:288px">Letterhead Two</div>

<!-- Envelope fronts -->
<div class="piece envelope" style="left:670px;top:43px">
  <svg viewBox="0 0 207 105" preserveAspectRatio="none">
    <path d="M0 0H207V12C150 8 80 2 0 10Z" fill="url(#navyFade)"/>
    <path d="M0 10C80 2 150 8 207 12V13.3C150 9.5 80 3.5 0 11.3Z" fill="var(--green)"/>
  </svg>
  <div class="brand">4nowvanta</div>
  <div class="contact">42 Juniper Street<br>Arlington, MA 02319</div>
</div>
<div class="label" style="left:750px;top:151px">Envelope Front</div>

<div class="piece envelope" style="left:672px;top:158px">
  <svg viewBox="0 0 207 105" preserveAspectRatio="none">
    <path d="M0 0H207V12C150 8 80 2 0 10Z" fill="url(#navyFade)"/>
    <path d="M0 10C80 2 150 8 207 12V13.3C150 9.5 80 3.5 0 11.3Z" fill="var(--green)"/>
  </svg>
  <div class="brand">4nowvanta</div>
  <div class="contact">42 Juniper Street<br>Arlington, MA 02319</div>
</div>
<div class="label" style="left:752px;top:266px">Envelope Front</div>

<!-- Envelope backs -->
<div class="piece envelope-back" style="top:34px">
  <svg viewBox="0 0 219 86" preserveAspectRatio="none">
    <path d="M0 0H219V30C160 40 120 52 109 54C98 52 60 40 0 30Z" fill="url(#navyFade)"/>
  </svg>
  <div class="brand on-dark">4nowvanta</div>
</div>
<div class="piece envelope-back" style="top:125px">
  <svg viewBox="0 0 219 86" preserveAspectRatio="none">
    <path d="M0 0H219V30C160 40 120 52 109 54C98 52 60 40 0 30Z" fill="var(--green)"/>
  </svg>
  <div class="brand on-dark">4nowvanta</div>
</div>
<div class="piece envelope-back" style="top:216px;height:72px">
  <svg viewBox="0 0 219 72" preserveAspectRatio="none">
    <path d="M0 0H219V26C160 34 120 44 109 46C98 44 60 34 0 26Z" fill="none" stroke="#d6d6d6" stroke-width="0.8"/>
  </svg>
  <div class="brand">4nowvanta</div>
</div>
<div class="label" style="left:998px;top:292px">Envelope Backs</div>
</body>
</html>
```